Poster for List of Company Values

We need a poster to outline our Values which will be displayed in our office as well as posted on our website and other platforms (so need to allow for some flexibly in its application).

File attached outlines what we currently have with design and also our company style guide.

Note that we are looking for a modern, clean look, which still represents our core activities of construction and environmental services.

You can also reference our website here:

https://corvellaworks.com.au/

Happy to answer any questions you might have.

Thanks for your interest,
Rhys

Target Market(s)

Internal and External clients

Industry/Entity Type

Construction, water and recycling

Font styles to use
Sans Serif

Requirements
Must have
• All values on the one page. Graphic to represent each value. Also needs to use company logo
Nice to have
• Preference for poster to be orientated in landscape
Should not have
• Do not follow example provided, this is only to demonstrate what we have to date and also the text required

```html
<!DOCTYPE html>
<html lang="en">
<head>
<meta charset="utf-8">
<title>Core Values – Corvella Works</title>
<link rel="stylesheet" href="https://fonts.googleapis.com/css2?family=Open+Sans:wght@700&family=Carlito:wght@400&display=swap">
<style>
  :root {
    --page: #ffffff;
    --brand-blue: #0d3f8e;
    --ink-light: #ffffff;
    --card-line: #e6ecf6;
    --icon-tone: #b9c9e6;
  }
  * { box-sizing: border-box; margin: 0; padding: 0; }
  html, body {
    width: 776px;
    height: 1200px;
    overflow: hidden;
    background: var(--page);
  }
  .poster {
    position: absolute;
    left: 28px;
    top: 27px;
    width: 738px;
    height: 1169px;
    background: var(--brand-blue);
    color: var(--ink-light);
  }
  .poster-title {
    position: absolute;
    left: 56px;
    top: 53px;
    font-family: "Open Sans", Arial, sans-serif;
    font-weight: 700;
    font-size: 43px;
    letter-spacing: 2.2px;
    line-height: 1;
  }
  .brand-name {
    position: absolute;
    left: 444px;
    top: 44px;
    display: flex;
    align-items: center;
    gap: 14px;
    font-family: "Open Sans", Arial, sans-serif;
    font-weight: 700;
    font-size: 27px;
    line-height: 1.05;
  }
  .brand-mark {
    width: 52px;
    height: 52px;
    background: var(--ink-light);
  }
  .values-grid {
    position: absolute;
    left: 53px;
    top: 168px;
    display: grid;
    grid-template-columns: 305px 305px;
    grid-template-rows: 301px 301px 301px;
    column-gap: 22px;
    row-gap: 21px;
  }
  .value-card {
    position: relative;
    border: 2px solid var(--card-line);
    text-align: center;
  }
  .value-title {
    position: absolute;
    left: 0;
    right: 0;
    top: 20px;
    font-family: "Open Sans", Arial, sans-serif;
    font-weight: 700;
    font-size: 33px;
    line-height: 42px;
    letter-spacing: 0.2px;
  }
  .value-icon {
    position: absolute;
    left: 50%;
    transform: translateX(-50%);
    background: var(--icon-tone);
    border-radius: 6px;
  }
  .value-text {
    position: absolute;
    left: 0;
    right: 0;
    bottom: 22px;
    font-family: "Carlito", Calibri, sans-serif;
    font-size: 15px;
    line-height: 17px;
  }
</style>
</head>
<body>
  <main class="poster">
    <h1 class="poster-title">CORE VALUES</h1>
    <div class="brand-name">
      <span class="brand-mark"></span>
      <span>CORVELLA<br>Works</span>
    </div>

    <section class="values-grid">
      <article class="value-card">
        <h2 class="value-title">BE<br>LOYAL</h2>
        <div class="value-icon" style="top:115px;width:100px;height:88px;" role="img" aria-label="Diamond icon"></div>
        <p class="value-text">We take care of our own and<br>provide opportunities to<br>listen and support each other</p>
      </article>

      <article class="value-card">
        <h2 class="value-title" style="top:15px;">BE OPEN<br>&amp; HONEST</h2>
        <div class="value-icon" style="top:117px;width:100px;height:88px;" role="img" aria-label="Icon of connected people network"></div>
        <p class="value-text" style="bottom:16px;">We are clear and open with each<br>other, and provide an approachable<br>and friendly environment</p>
      </article>

      <article class="value-card">
        <h2 class="value-title">SHOW<br>INITIATIVE</h2>
        <div class="value-icon" style="top:115px;width:66px;height:103px;" role="img" aria-label="Icon of a figure climbing stairs"></div>
        <p class="value-text" style="bottom:12px;">We celebrate and<br>recognize our own andencourage<br>forward thinking</p>
      </article>

      <article class="value-card">
        <h2 class="value-title" style="top:29px;">BE<br>POSITIVE</h2>
        <div class="value-icon" style="top:125px;width:82px;height:80px;" role="img" aria-label="Thumbs up icon"></div>
        <p class="value-text" style="bottom:12px;">We celebrate and recognize<br>our own and encourage<br>forward thinking</p>
      </article>

      <article class="value-card">
        <h2 class="value-title" style="top:30px;">THINK<br>TEAM</h2>
        <div class="value-icon" style="top:140px;width:98px;height:59px;" role="img" aria-label="Team of three people icon"></div>
        <p class="value-text">We communicate effectively<br>and work as a team by helping and<br>supporting each other</p>
      </article>

      <article class="value-card">
        <h2 class="value-title" style="top:30px;">SHOW<br>RESPECT</h2>
        <div class="value-icon" style="top:137px;width:105px;height:65px;" role="img" aria-label="Handshake icon"></div>
        <p class="value-text" style="bottom:40px;">We Value The Diversity<br>And Opinions Of All</p>
      </article>
    </section>
  </main>
</body>
</html>
```